"Dario Quillon" Business Card

Friends

My name is "Dario Quillon" and I need your help! I need a new business card for my personal use.

As background, "Dario Quillon" is actually an alias that I use when I meet women. Please use your creative skills to create an amazing business card for me to use!

In addition to including my name and contact details (see the "Must Have" section), you may wish to add a catchphrase or a title if you think it would help me :)

For background, please see:

http://www.dailybrightwire.com/2013/07/23/morton-feld-dario-quillon_n_5129847.html

Looking forward to seeing what you can do for me.

Hugs and kisses,

Dario Quillon [courtesy of PixelHarbor]

Target Market(s)

Adult women in New York City...or anywhere really.

Industry/Entity Type

Business

Requirements
Must have
• Please include the following details:

Dario Quillon
P: +1-555-3QUILLN
E: secrets@darioquillon-mail.com
Nice to have
• You might include a catchphrase, like "Quillon is my surname But you can call me Mr Smoothstep".

Or perhaps a title, like "Dario Quillon, Head of Sexy Times".

You're creative...I will leave the details to you my friends.
Should not have
• Any references to my actual name...because then, what's the point in using an alias?

```html
<!DOCTYPE html>
<html lang="en">
<head>
<meta charset="utf-8">
<title>Dario Quillon — Business Card</title>
<link rel="stylesheet" href="https://fonts.googleapis.com/css2?family=Questrial&family=Tinos&family=Courier+Prime&display=swap">
<style>
  :root {
    --ink: #000000;
    --paper-text: #ffffff;
    --rule: #d8d8d8;
    --metal-light: #fbfbf2;
    --metal-mid: #c9c6ad;
    --metal-dark: #6d6a55;
    --metal-edge: #2a291f;
    --denim-deep: #0b1320;
    --denim: #2a3f5e;
    --denim-light: #6f8db3;
    --skin: #b9825a;
    --skin-light: #dca77c;
  }
  html, body {
    margin: 0;
    padding: 0;
    width: 1200px;
    height: 800px;
    overflow: hidden;
    background: var(--ink);
  }
  .card {
    position: relative;
    width: 1200px;
    height: 800px;
    background: var(--ink);
    overflow: hidden;
  }
  .hero-photo {
    position: absolute;
    left: 0;
    top: 190px;
    width: 1200px;
    height: 610px;
    background:
      radial-gradient(ellipse 420px 90px at 560px 380px, var(--skin-light) 0%, var(--skin) 45%, rgba(185,130,90,0) 100%),
      radial-gradient(ellipse 380px 220px at 1090px 300px, var(--denim-light) 0%, var(--denim) 45%, rgba(42,63,94,0) 100%),
      radial-gradient(ellipse 360px 260px at 140px 330px, var(--denim) 0%, rgba(42,63,94,0) 100%),
      linear-gradient(180deg, var(--ink) 0%, var(--denim-deep) 30%, var(--denim-deep) 75%, var(--ink) 100%);
  }
  .name {
    position: absolute;
    left: 0;
    top: 0;
    width: 1200px;
    height: 140px;
    margin: 0;
  }
  .name-text {
    font-family: "Questrial", sans-serif;
    font-size: 100px;
    fill: url(#name-metal);
    stroke: var(--metal-edge);
    stroke-width: 2px;
    paint-order: stroke;
  }
  .name-rule {
    position: absolute;
    left: 60px;
    top: 142px;
    width: 1087px;
    height: 1px;
    background: var(--rule);
  }
  .contact {
    position: absolute;
    left: 53px;
    top: 259px;
    margin: 0;
    font-family: "Tinos", serif;
    font-size: 68px;
    line-height: 80px;
    color: var(--paper-text);
    white-space: nowrap;
  }
  .contact span { display: block; }
  .tagline {
    position: absolute;
    left: 0;
    bottom: 20px;
    width: 1200px;
    margin: 0;
    text-align: center;
    font-family: "Courier Prime", monospace;
    font-size: 32px;
    line-height: 40px;
    color: var(--paper-text);
    white-space: nowrap;
  }
</style>
</head>
<body>
  <div class="card">
    <div class="hero-photo" role="img" aria-label="Photograph of a shirtless man in an open denim shirt and jeans lying back against a dark background"></div>
    <h1 class="name">
      <svg width="1200" height="140" viewBox="0 0 1200 140" aria-label="Dario Quillon">
        <defs>
          <linearGradient id="name-metal" x1="0" y1="0" x2="0" y2="1">
            <stop offset="0" stop-color="var(--metal-light)"/>
            <stop offset="0.55" stop-color="var(--metal-mid)"/>
            <stop offset="1" stop-color="var(--metal-dark)"/>
          </linearGradient>
        </defs>
        <text class="name-text" x="60" y="114" textLength="1087" lengthAdjust="spacingAndGlyphs">DARIO QUILLON</text>
      </svg>
    </h1>
    <div class="name-rule"></div>
    <p class="contact">
      <span class="contact-phone">+1-555-3QUILLN</span>
      <span class="contact-email">secrets@darioquillon-mail.com</span>
    </p>
    <p class="tagline">be with quillon, enjoy with quillon it doesn’t happen always</p>
  </div>
</body>
</html>
```